HIGH-END ANTI AGING START-UP NEEDS DOCUMENT/LETTERHEAD DESIGN!!!!

We are a high end anti-aging and health start-up catering to clients in Stamford and NYC. We just did a logo redesign and are now looking for a letter head design that we can use IN GOOGLE DOCS for marrowfieldcaregroup.example clients. We are REALLY EXCITED to see what you can show us!!!!!!!! We need something sophisticated and MODERN! Thanks so much!

Target Market(s)

High end, boutique medical clients. Our clientele is fairly high profile and we need a sleek, sophisticated letter head to put on all of our marketing materials and medical forms as well.

Industry/Entity Type

Medical

Font styles to use
Serif
Sans Serif

Colors
0255a3
ffffff
00a990
1b1b1b
919191

Requirements
Must have
• Must have the logo and "Marrowfield Care Group" written somewhere. Must have our URL www.marrowfieldcaregroup.example.
Nice to have
• office phone number (555) 374-9102
Should not have
• Colors outside of our logo colors + grey + black

```html
<!DOCTYPE html>
<html lang="en">
<head>
<meta charset="utf-8">
<title>Marrowfield Care Group — Letterhead</title>
<link href="https://fonts.googleapis.com/css2?family=Fira+Sans:wght@400;500&family=Lato:wght@300;400&family=Libre+Baskerville:wght@700&display=swap" rel="stylesheet">
<style>
  :root {
    --brand-blue: #4f80e0;
    --brand-green: #159649;
    --ink: #1b1b1b;
    --ink-soft: #555b63;
    --paper: #f6f6f6;
    --backdrop: #8fb3e6;
  }
  * { box-sizing: border-box; margin: 0; padding: 0; }
  html, body {
    width: 1200px; height: 1200px; overflow: hidden;
    background: var(--backdrop);
  }
  .letterhead {
    position: absolute; left: 190px; top: 20px;
    width: 820px; height: 1160px;
    background: var(--paper);
    box-shadow: 0 4px 18px rgba(20, 40, 90, .25);
    overflow: hidden;
  }
  .header-band { position: absolute; left: 0; top: 0; width: 820px; height: 170px; }
  .brand-name {
    position: absolute; left: 0; right: 0; top: 182px;
    text-align: center;
    font-family: "Libre Baskerville", Georgia, serif;
    font-weight: 700; font-size: 21px; letter-spacing: .5px;
    color: var(--brand-blue);
  }
  .recipient {
    position: absolute; left: 77px; top: 278px;
    font-family: "Fira Sans", sans-serif; color: var(--ink);
  }
  .recipient-name { font-weight: 500; font-size: 16px; letter-spacing: .4px; }
  .recipient-title { font-size: 16px; margin-top: 7px; color: var(--ink-soft); letter-spacing: .4px; }
  .letter-meta {
    position: absolute; right: 76px; top: 279px; text-align: right;
    font-family: "Lato", sans-serif; font-size: 15px; line-height: 20px; color: var(--ink);
  }
  .letter-body {
    position: absolute; left: 77px; width: 667px; top: 347px;
    font-family: "Lato", sans-serif; font-weight: 300; font-size: 16.2px;
    line-height: 22.6px; color: #3d4249; text-align: justify;
  }
  .letter-body p { margin-bottom: 22.6px; }
  .sign-off {
    position: absolute; left: 77px; top: 863px;
    font-family: "Lato", sans-serif; font-weight: 300; font-size: 15px; color: #3d4249;
  }
  .signer { position: absolute; left: 77px; top: 897px; font-family: "Fira Sans", sans-serif; color: var(--ink); }
  .signer-name { font-size: 14.5px; letter-spacing: .6px; }
  .signer-role { font-size: 11.5px; letter-spacing: .8px; margin-top: 2px; color: var(--ink-soft); }
  .contact-line {
    position: absolute; left: 0; right: 0; top: 1070px;
    display: flex; justify-content: center; align-items: center; gap: 14px;
    font-family: "Lato", sans-serif; font-size: 13.5px; color: var(--ink);
  }
  .contact-item { display: flex; align-items: center; gap: 10px; }
  .contact-item svg { width: 11px; height: 11px; fill: var(--brand-blue); }
  .address-line {
    position: absolute; left: 0; right: 0; top: 1096px; text-align: center;
    font-family: "Lato", sans-serif; font-size: 13.5px; color: var(--ink);
  }
  .footer-bar { position: absolute; left: 0; bottom: 0; width: 100%; height: 14px; display: flex; }
  .footer-bar .bar-green { flex: 1; background: var(--brand-green); }
  .footer-bar .bar-blue { flex: 1; background: var(--brand-blue); }
</style>
</head>
<body>
  <main class="letterhead">
    <svg class="header-band" viewBox="0 0 820 170" aria-hidden="true">
      <path d="M0 0 H820 V67 Q410 157 0 67 Z" fill="var(--brand-blue)"/>
      <path d="M32 76 Q410 166 788 76" fill="none" stroke="var(--brand-green)" stroke-width="3"/>
      <circle cx="410" cy="112" r="53" fill="var(--brand-green)" stroke="#ffffff" stroke-width="5"/>
    </svg>
    <div class="brand-name">Marrowfield Care Group</div>

    <div class="recipient">
      <div class="recipient-name">Dear, Delia Renwick</div>
      <div class="recipient-title">Creative Director</div>
    </div>
    <div class="letter-meta">
      <div>Date: 12.05.2017</div>
      <div>Stamford CT</div>
    </div>

    <section class="letter-body">
      <p>Lorem ipsum dolor sit amet, consectetuer adipiscing elit, sed diam nonummy nibh euismod tincidunt ut laoreet dolore magna aliquam erat volutpat. Ut wisi enim ad minim veniam, quis nostrud exerci tation ullamcorper suscipit lobortis nisl ut aliquip ex ea commodo consequat. Duis autem vel eum iriure dolor in hendrerit in vulputate velit esse molestie consequat, vel illum dolore eu feugiat nulla facilisis at vero eros et accumsan et iusto odio dignissim qui blandit praesent luptatum zzril delenit augue duis dolore te feugait nulla facilisi.</p>
      <p>Lorem ipsum dolor sit amet, cons ectetuer adipiscing elit, sed diam nonummy nibh euismod tincidunt ut laoreet dolore magna aliquam erat volutpat. Ut wisi enim ad minim veniam, quis nostrud exerci tation ullamcorper suscipit lobortis nisl ut aliquip ex ea commodo consequat. Lorem ipsum dolor sit amet, consectetuer adipiscing elit, sed diam nonummy nibh euismod tincidunt ut laoreet dolore magna aliquam erat volutpat. Ut wisi enim ad minim veniam, quis nostrud exerci tation ullamcorper suscipit lobortis.</p>
      <p>nisl ut aliquip ex ea commodo consequat. Duis autem vel eum iriure dolor in hendrerit in vulputate velit esse molestie consequat, vel illum dolore eu feugiat nulla facilisis at vero eros et accumsan et iusto odio dignissim qui blandit praesent luptatum zzril delenit augue duis dolore te feugait nulla facilisi.</p>
      <p>tincidunt ut laoreet dolore magna aliquam erat volutpat. Ut wisi enim ad minim veniam, quis nostrud exerci tation ullamcorper suscipit lobortis nisl ut aliquip ex ea commodo consequat.</p>
    </section>

    <div class="sign-off">Regards,</div>
    <div class="signer">
      <div class="signer-name">Corwin Vale</div>
      <div class="signer-role">EXECUTIVE DIRECTOR</div>
    </div>

    <footer>
      <div class="contact-line">
        <span class="contact-item">
          <svg viewBox="0 0 24 24" aria-hidden="true"><path d="M6.6 10.8a15.1 15.1 0 0 0 6.6 6.6l2.2-2.2c.3-.3.7-.4 1-.2 1.1.4 2.3.6 3.6.6.6 0 1 .4 1 1V20c0 .6-.4 1-1 1A17 17 0 0 1 3 4c0-.6.4-1 1-1h3.5c.6 0 1 .4 1 1 0 1.3.2 2.5.6 3.6.1.3 0 .7-.2 1z"/></svg>
          (555) 374-9102
        </span>
        <span class="contact-item">
          <svg viewBox="0 0 24 24" aria-hidden="true"><path d="M3 5h18v14H3zM5 7v.5l7 4.5 7-4.5V7zm0 2.9V17h14V9.9l-7 4.5z"/></svg>
          Info@marrowfieldcaregroup.example
        </span>
        <span class="contact-item">
          <svg viewBox="0 0 24 24" aria-hidden="true"><path d="M12 2a10 10 0 1 0 0 20 10 10 0 0 0 0-20zm0 3a7 7 0 0 1 6.9 6h-3.5a11 11 0 0 0-1.6-5.8A7 7 0 0 1 12 5zm-1.8.2A11 11 0 0 0 8.6 11H5.1a7 7 0 0 1 5.1-5.8zM5.1 13h3.5a11 11 0 0 0 1.6 5.8A7 7 0 0 1 5.1 13zm8.7 5.8a11 11 0 0 0 1.6-5.8h3.5a7 7 0 0 1-5.1 5.8z"/></svg>
          www.marrowfieldcaregroup.example
        </span>
      </div>
      <div class="address-line">Marrowfield Care Group, 18 Linden Ave. Suite 410, Stamford CT, 06900</div>
      <div class="footer-bar"><span class="bar-green"></span><span class="bar-blue"></span></div>
    </footer>
  </main>
</body>
</html>
```